Esoteric, wellness company labels

Verdant Lumen is a lifestyle brand with multiple products. We have an offshoot as well called Lumen Coffee. I need multiple labels or packaging designs that all match so I can start wholesaling.

I want something fun and very eye catching. I have two different logos for Verdant Lumen but just one for the coffee. I’m
Undecided which one I want on the labels because I like both. So either would work. Any coffee products go under lumen coffee and any other products go under Verdant Lumen.

We sell items such as crystals, tarot and oracle decks, candles, organic coffee, superfood powders and herbs and more.

The items I need labels for should have a streamline look so that all are recognizable as the Verdant Lumen brand. The products that are a priority are:
Organic coffee
Reishi infused coffee
Lion’s Mane infused coffee
Those go under Lumen Coffee.

Soon I’ll do more items;
Sacred smudging spray
Sacred smudging cleaner
Multiple superfoods
Etc
Updates

We have decided to use compostable coffee bags that are approximately 9x6x33cm so your standard 1lb bag you would see in a store. We still want colorful and eye catching but at the same time being eco friendly. The coffee is 100% organic, free trade, low acid.

We are looking for labels for the coffee but also want to be able to use the same kind of design or similar down the road for our other products. We carry superfood powders (lion’s mane, blue Spirulina, reishi, pearl powder, sea moss etc) but also things like smudging spray, rose water, neroli water, essential oils etc. we are a lifestyle company so we are looking for labels across our store brand items.

Target Market(s)

Esoteric, health and wellness, “new age”

Industry/Entity Type

Retail, wellness,

Colors

Designer to choose colors to be used in the design.

Requirements
Must have
• Beauty, attraction
Should not have
• Anything to do with religion, no dark witchy themes

```html
<!DOCTYPE html>
<html lang="en">
<head>
<meta charset="utf-8">
<title>Lumen Coffee — Label Range</title>
<link rel="stylesheet" href="https://fonts.googleapis.com/css2?family=Josefin+Sans:wght@300&family=Cormorant+Garamond:wght@500;700&display=swap">
<style>
  :root {
    --paper: #efe0d6;
    --cream: #f1e2d8;
    --rose: #c1717f;
    --navy: #404e5f;
    --olive: #8b8678;
  }
  * { margin: 0; padding: 0; box-sizing: border-box; }
  html, body {
    width: 1200px;
    height: 720px;
    overflow: hidden;
    background: var(--paper);
  }
  .label-range {
    width: 1200px;
    height: 720px;
    display: flex;
    align-items: center;
    justify-content: center;
    gap: 60px;
  }
  .label {
    width: 330px;
    height: 477px;
    display: block;
  }
  .label--organic { --label-ink: var(--rose); }
  .label--reishi  { --label-ink: var(--navy); }
  .label--lions-mane { --label-ink: var(--olive); }

  .label-body { fill: var(--label-ink); }
  .frame-line { fill: none; stroke: var(--cream); }
  .frame-line--bold { stroke-width: 3; }
  .frame-line--fine { stroke-width: 1.4; }
  .banner { fill: none; stroke: var(--cream); stroke-width: 2.5; }
  .banner-dot, .frame-dot { fill: var(--cream); }
  .mark-circle { fill: none; stroke: var(--cream); stroke-width: 1.6; }
  .maker-box { fill: none; stroke: var(--cream); stroke-width: 1.4; }

  .brand-name {
    font-family: "Josefin Sans", sans-serif;
    font-weight: 300;
    fill: var(--cream);
    text-anchor: middle;
  }
  .brand-name--main { font-size: 31px; letter-spacing: 9px; }
  .brand-name--maker { font-size: 24px; letter-spacing: 5px; }
  .brand-name--maker-sub { font-size: 9px; letter-spacing: 7px; }

  .product-name {
    font-family: "Cormorant Garamond", serif;
    font-weight: 700;
    fill: var(--cream);
    text-anchor: middle;
  }
  .product-name--large { font-size: 66px; }
  .product-name--mid { font-size: 40px; }
  .product-name--small { font-size: 30px; }

  .site-address {
    font-family: "Cormorant Garamond", serif;
    font-weight: 500;
    font-size: 15px;
    letter-spacing: 0.5px;
    fill: var(--cream);
    text-anchor: middle;
  }
</style>
</head>
<body>
<main class="label-range">

  <svg class="label label--organic" viewBox="0 0 450 650" role="img" aria-label="Organic coffee label, rose field with a soft floral damask pattern">
    <path class="label-body" d="M0,52 H26 V34 H118 Q225,-16 332,34 H424 V52 H450 V598 H424 V616 H332 Q225,666 118,616 H26 V598 H0 Z"/>
    <path class="frame-line frame-line--bold" d="M14,64 H38 V46 H124 Q225,0 326,46 H412 V64 H436 V586 H412 V604 H326 Q225,650 124,604 H38 V586 H14 Z"/>
    <path class="frame-line frame-line--fine" d="M24,72 H46 V56 H128 Q225,12 322,56 H404 V72 H426 V578 H404 V594 H322 Q225,638 128,594 H46 V578 H24 Z"/>
    <circle class="frame-dot" cx="225" cy="46" r="3"/>
    <circle class="frame-dot" cx="225" cy="604" r="3"/>
    <circle class="mark-circle" cx="225" cy="118" r="40"/>
    <text class="brand-name brand-name--main" x="229" y="214">LUMEN</text>
    <text class="brand-name brand-name--main" x="229" y="246">COFFEE</text>
    <rect class="maker-box" x="138" y="258" width="174" height="58"/>
    <text class="brand-name brand-name--maker" x="227" y="292">VERDANT</text>
    <text class="brand-name brand-name--maker-sub" x="228" y="307">LUMEN</text>
    <path class="banner" d="M40,378 H410 L384,442 L408,512 H42 L66,442 Z"/>
    <circle class="banner-dot" cx="52" cy="446" r="7"/>
    <circle class="banner-dot" cx="398" cy="446" r="7"/>
    <text class="product-name product-name--large" x="225" y="445">ORGANIC</text>
    <text class="product-name product-name--large" x="225" y="502">COFFEE</text>
    <text class="site-address" x="225" y="560">VERDANTLUMEN.COM</text>
  </svg>

  <svg class="label label--reishi" viewBox="0 0 450 650" role="img" aria-label="Reishi infused coffee label, slate blue field with a soft floral damask pattern">
    <path class="label-body" d="M0,52 H26 V34 H118 Q225,-16 332,34 H424 V52 H450 V598 H424 V616 H332 Q225,666 118,616 H26 V598 H0 Z"/>
    <path class="frame-line frame-line--bold" d="M14,64 H38 V46 H124 Q225,0 326,46 H412 V64 H436 V586 H412 V604 H326 Q225,650 124,604 H38 V586 H14 Z"/>
    <path class="frame-line frame-line--fine" d="M24,72 H46 V56 H128 Q225,12 322,56 H404 V72 H426 V578 H404 V594 H322 Q225,638 128,594 H46 V578 H24 Z"/>
    <circle class="frame-dot" cx="225" cy="46" r="3"/>
    <circle class="frame-dot" cx="225" cy="604" r="3"/>
    <circle class="mark-circle" cx="225" cy="118" r="40"/>
    <text class="brand-name brand-name--main" x="229" y="214">LUMEN</text>
    <text class="brand-name brand-name--main" x="229" y="246">COFFEE</text>
    <rect class="maker-box" x="138" y="258" width="174" height="58"/>
    <text class="brand-name brand-name--maker" x="227" y="292">VERDANT</text>
    <text class="brand-name brand-name--maker-sub" x="228" y="307">LUMEN</text>
    <path class="banner" d="M40,378 H410 L384,442 L408,512 H42 L66,442 Z"/>
    <circle class="banner-dot" cx="52" cy="446" r="7"/>
    <circle class="banner-dot" cx="398" cy="446" r="7"/>
    <text class="product-name product-name--mid" x="225" y="424">REISHI INFUSED</text>
    <text class="product-name product-name--large" x="225" y="494">COFFEE</text>
    <text class="site-address" x="225" y="560">VERDANTLUMEN.COM</text>
  </svg>

  <svg class="label label--lions-mane" viewBox="0 0 450 650" role="img" aria-label="Lion's mane infused coffee label, warm olive field with a soft floral damask pattern">
    <path class="label-body" d="M0,52 H26 V34 H118 Q225,-16 332,34 H424 V52 H450 V598 H424 V616 H332 Q225,666 118,616 H26 V598 H0 Z"/>
    <path class="frame-line frame-line--bold" d="M14,64 H38 V46 H124 Q225,0 326,46 H412 V64 H436 V586 H412 V604 H326 Q225,650 124,604 H38 V586 H14 Z"/>
    <path class="frame-line frame-line--fine" d="M24,72 H46 V56 H128 Q225,12 322,56 H404 V72 H426 V578 H404 V594 H322 Q225,638 128,594 H46 V578 H24 Z"/>
    <circle class="frame-dot" cx="225" cy="46" r="3"/>
    <circle class="frame-dot" cx="225" cy="604" r="3"/>
    <circle class="mark-circle" cx="225" cy="118" r="40"/>
    <text class="brand-name brand-name--main" x="229" y="214">LUMEN</text>
    <text class="brand-name brand-name--main" x="229" y="246">COFFEE</text>
    <rect class="maker-box" x="138" y="258" width="174" height="58"/>
    <text class="brand-name brand-name--maker" x="227" y="292">VERDANT</text>
    <text class="brand-name brand-name--maker-sub" x="228" y="307">LUMEN</text>
    <path class="banner" d="M40,378 H410 L384,442 L408,512 H42 L66,442 Z"/>
    <circle class="banner-dot" cx="52" cy="446" r="7"/>
    <circle class="banner-dot" cx="398" cy="446" r="7"/>
    <text class="product-name product-name--small" x="225" y="416">LION’S MANE INFUSED</text>
    <text class="product-name product-name--large" x="225" y="494">COFFEE</text>
    <text class="site-address" x="225" y="560">VERDANTLUMEN.COM</text>
  </svg>

</main>
</body>
</html>
```